We need visit card and a letter paper for our website. thx

We have a beauty clinic in Switzerland.
https://wolkenbachtal.ch
We need a visit card.

Requirements
Must have
• see colors on website

```html
<!DOCTYPE html>
<html lang="de">
<head>
<meta charset="utf-8">
<title>Wolkenbachtal Beauty Clinic – Visitenkarte</title>
<link rel="stylesheet" href="https://fonts.googleapis.com/css2?family=Roboto:wght@400;500&family=Roboto+Condensed:wght@700&family=Josefin+Sans:wght@400&display=swap">
<style>
  :root {
    --rose: #cf4b7b;
    --rose-light: #e7aac2;
    --ink: #222222;
    --paper: #ffffff;
  }
  * { margin: 0; padding: 0; box-sizing: border-box; }
  html, body {
    width: 1200px; height: 686px; overflow: hidden;
    background: var(--paper);
  }
  .card {
    position: relative; width: 1200px; height: 686px;
    background: var(--paper); overflow: hidden;
    font-family: "Roboto", Arial, sans-serif; color: var(--ink);
  }
  .side-waves { position: absolute; inset: 0; width: 1200px; height: 686px; }
  .side-waves path { fill: var(--rose); }

  .brand {
    position: absolute; left: 0; top: 112px; width: 1200px;
    display: flex; justify-content: center; align-items: center; gap: 18px;
  }
  .brand-mark { width: 18px; height: 18px; background: var(--ink); }
  .brand-name {
    font-family: "Josefin Sans", Arial, sans-serif; font-weight: 400;
    font-size: 64px; line-height: 1; color: var(--ink); letter-spacing: 1px;
  }

  .tagline {
    position: absolute; left: 0; top: 318px; width: 1200px; text-align: center;
    font-family: "Roboto Condensed", Arial, sans-serif; font-weight: 700;
    font-size: 24px; color: var(--ink);
  }
  .headline {
    position: absolute; left: 42px; top: 361px; width: 1116px; height: 87px;
    border-radius: 44px; background: var(--rose); color: var(--paper);
    display: flex; align-items: center; justify-content: center;
    font-size: 47px; font-weight: 400;
  }
  .rule { position: absolute; height: 2px; background: var(--rose-light); }
  .rule-upper { left: 177px; top: 470px; width: 994px; }
  .rule-lower { left: 31px; top: 542px; width: 1020px; }

  .services {
    position: absolute; top: 486px; left: 261px; display: flex; gap: 7px;
    list-style: none;
  }
  .service {
    height: 43px; border: 1px solid #555; color: var(--rose);
    font-size: 27px; display: flex; align-items: center; justify-content: center;
  }
  .service-breast { width: 222px; }
  .service-lipo { width: 222px; }
  .service-intimate { width: 221px; margin-left: 2px; }

  .contact-intro {
    position: absolute; left: 46px; top: 601px; font-size: 22px; line-height: 29px;
  }
  .divider {
    position: absolute; left: 536px; top: 594px; width: 1px; height: 77px;
    background: var(--rose-light);
  }
  .contact-details {
    position: absolute; left: 571px; top: 587px; font-size: 23px; line-height: 27px;
    font-style: normal;
  }
</style>
</head>
<body>
  <main class="card">
    <svg class="side-waves" viewBox="0 0 1200 686" aria-hidden="true">
      <path d="M0 0 H92 C70 80 40 150 30 230 C20 300 35 360 50 430 C65 500 85 600 80 686 H0 Z"/>
      <path d="M1168 0 H1200 V686 H1142 C1175 600 1185 520 1175 440 C1165 380 1160 320 1172 250 C1185 170 1190 80 1168 0 Z"/>
    </svg>

    <header class="brand">
      <span class="brand-mark"></span>
      <span class="brand-name">Wolkenbachtal</span>
    </header>

    <p class="tagline">Wolkenbachtal – Beauty Clinic Wolkenbach/Schweiz</p>
    <h1 class="headline">Schönheitsklinik für Plastische Chirurgie</h1>

    <div class="rule rule-upper"></div>
    <ul class="services">
      <li class="service service-breast">Brustchirurgie</li>
      <li class="service service-lipo">Fettabsaugung</li>
      <li class="service service-intimate">Intimbereich</li>
    </ul>
    <div class="rule rule-lower"></div>

    <p class="contact-intro">Nehmen Sie Kontakt auf!<br>Dr. Lena Marbach &amp; Dr. Tobias Reinhold, DESA</p>
    <div class="divider"></div>
    <address class="contact-details">
      Talweg 14, 7099 Wolkenbach, Switzerland<br>
      gratis 24h Schönheits-Hotline: +41 (0) 800 55 20 20<br>
      E-Mail: hallo@wolkenbachtal.ch
    </address>
  </main>
</body>
</html>
```